Modern Business Card Design Needed for Young Realtor

Information that is going on the card:Marvin Pold
Broker/Owner
555.210.3367
Marvin@MPoldRealty.com
www.MPoldRealty.com

Would also like to include my Instagram Handle somewhere. Probably on the back: the_queencity_realtorMy previous business card is attached, I like that one but would like an updated version and maybe a few design changes

Marvin Pold
Broker/Owner
555.210.3367
Marvin@MPoldRealty.com
www.MPoldRealty.com

• Would also like to include my Instagram Handle somewhere. Probably on the back: the_pinecrest_realtor
• Dorrance Hale or the DH (logo from the previous card.)

```html
<!DOCTYPE html>
<html lang="en">
<head>
<meta charset="utf-8">
<title>MPold Realty Business Card</title>
<link href="https://fonts.googleapis.com/css2?family=Roboto:wght@400;700;900&display=swap" rel="stylesheet">
<style>
  :root {
    --bg: #2a2a2a;
    --card-dark: #1c1c1d;
    --card-light: #ffffff;
    --brand-red: #b01f2e;
    --ink: #1e1e1e;
    --muted: #d9d9d9;
    --photo-a: #6f8f55;
    --photo-b: #9aa38a;
    --photo-c: #5d6066;
  }
  * { margin: 0; padding: 0; box-sizing: border-box; }
  html, body { width: 1200px; height: 895px; overflow: hidden; }
  body {
    background: var(--bg);
    display: flex;
    flex-direction: column;
    align-items: center;
    justify-content: center;
    gap: 36px;
    font-family: "Roboto", Arial, sans-serif;
  }
  .card { width: 660px; height: 377px; position: relative; overflow: hidden; }

  /* Back */
  .card-back { background: var(--card-dark); }
  .back-texture {
    position: absolute; left: 70px; top: 50px; width: 520px; height: 240px;
    background: radial-gradient(ellipse at center, rgba(255,255,255,0.06), rgba(255,255,255,0) 70%);
  }
  .brand {
    position: absolute; left: 0; right: 0; top: 150px;
    display: flex; justify-content: center; align-items: center; gap: 14px;
  }
  .brand-mark { width: 14px; height: 14px; border-radius: 50%; background: var(--muted); }
  .brand-name {
    font-family: "Roboto", Arial, sans-serif;
    font-weight: 700; font-size: 40px; color: var(--card-light);
  }
  .handle {
    position: absolute; left: 0; right: 0; top: 238px;
    display: flex; justify-content: center; align-items: center; gap: 10px;
    font-family: "Roboto", Arial, sans-serif; font-size: 15px; color: var(--muted);
  }
  .handle-mark { width: 12px; height: 12px; background: var(--muted); }

  /* Front */
  .card-front { background: var(--card-light); display: flex; }
  .front-info { width: 330px; padding: 50px 0 0 42px; }
  .badges { display: flex; gap: 10px; margin-bottom: 20px; }
  .badge { width: 34px; height: 30px; background: var(--ink); }
  .badge-square { width: 30px; }
  .agent-name {
    font-weight: 900; font-size: 30px; color: var(--brand-red);
    text-transform: uppercase; letter-spacing: 0.3px;
  }
  .agent-title { font-size: 16px; color: var(--ink); margin-bottom: 22px; }
  .address { font-size: 15px; color: var(--ink); line-height: 1.3; margin-bottom: 10px; }
  .contact-list { list-style: none; }
  .contact-list li {
    display: flex; align-items: center; gap: 10px;
    font-size: 15px; color: var(--ink); line-height: 1.45;
  }
  .contact-list svg { width: 12px; height: 12px; flex: none; fill: var(--brand-red); }
  .divider { width: 4px; background: var(--brand-red); }
  .portrait {
    flex: 1;
    background: linear-gradient(160deg, var(--photo-a) 0%, var(--photo-b) 55%, var(--photo-c) 100%);
  }
</style>
</head>
<body>

<section class="card card-back">
  <div class="back-texture" role="img" aria-label="Faint dotted world map pattern"></div>
  <div class="brand">
    <span class="brand-mark"></span>
    <span class="brand-name">MPold Realty</span>
  </div>
  <div class="handle"><span class="handle-mark"></span>the_pinecrest_realtor</div>
</section>

<section class="card card-front">
  <div class="front-info">
    <div class="badges">
      <span class="badge"></span>
      <span class="badge badge-square"></span>
    </div>
    <h1 class="agent-name">Marvin Pold</h1>
    <p class="agent-title">Broker/Owner</p>
    <p class="address">1180 Larkspur Way Ste. 200<br>Ashford, NC 28000</p>
    <ul class="contact-list">
      <li><svg viewBox="0 0 12 12"><path d="M2 0h3l1 3-2 1a7 7 0 0 0 4 4l1-2 3 1v3a2 2 0 0 1-2 2A10 10 0 0 1 0 2a2 2 0 0 1 2-2z"/></svg>555.210.3367</li>
      <li><svg viewBox="0 0 12 12"><rect x="3" y="0" width="6" height="4"/><rect x="0" y="4" width="12" height="5" rx="1"/><rect x="3" y="8" width="6" height="4"/></svg>555.210.4418</li>
      <li><svg viewBox="0 0 12 12"><path d="M0 2h12v1L6 7 0 3z"/><path d="M0 4.5l6 4 6-4V10H0z"/></svg>Marvin@MPoldRealty.com</li>
      <li><svg viewBox="0 0 12 12"><circle cx="6" cy="6" r="5.2" fill="none" stroke="#b01f2e" stroke-width="1.4"/><path d="M1 6h10M6 1v10" stroke="#b01f2e" stroke-width="1"/></svg>www.MPoldRealty.com</li>
    </ul>
  </div>
  <div class="divider"></div>
  <div class="portrait" role="img" aria-label="Portrait photo of the broker in a grey blazer outdoors"></div>
</section>

</body>
</html>
```